Site Re-Design For IT/Internet Services Site

Hi, We need a redevopment of our existing website (www.talvrek.com)
Pages That need designing are:
- Content Page (existing page: http://www.talvrek.com)
- Hotspot Locations Page (existing page: Http://www.talvrek.com/hotspot-locations/hotspot-locations.asp)
- Form page layout, including textbox, checkbox, radio buttons, drop down, submit/reset buttons, "required fields error message"
- Design of our subscription "plan selection" content page (https://secure.talvrek.com/?location=1001)
- Design of the NEXT TWO pages in the above subscription form, the "email/password page, to see this select less than 3 months, 1 hour, then continue and also the credit card page, see this by filling out left hand side "new account" form and continue Specs:
- The same navigation will be retained, but should be easily modifyable via PSD file.

- NOTE THAT FOR THE DESIGN COMPETITION, ONLY the CONTENT PAGE needs to be designed

- Existing Logo to Be Maintained and COMPLETELY UNCHANGE IN ANY ASPECT
- Similar format of dual navigation required. Currently main nav is horizontal with sub nav below, and "extra" nav available on left vertical strip. Does have to stay in this format, however main nav with subnav, and "extra" nav spots must be available
- Design should be fresh and innovative
- Colors are negotiable however typical design nono's will not be accepted (black content area etc) Code Requirements:
- PSD file should contain overall design, as well as sub PSD files for navigation to be easily re-created at a later date where required.

By negotiation after sucessful design chosen, extra design aspects such as: psd cutup in html, HTML markup compatible with IE6+, Chrome, Firefox required - Seperate CSS stylesheet - Images in sub folders as appropriate may be required.

Internet

5+ pages

• black background, etc.

```html
<!DOCTYPE html>
<html lang="en">
<head>
<meta charset="utf-8">
<title>Talvrek Wireless Hotspots Australia</title>
<link rel="stylesheet" href="https://fonts.googleapis.com/css2?family=Krona+One&family=Arimo:wght@400;700&family=Quicksand:wght@500;700&display=swap">
<style>
:root{
  --lime:#a9c51c;
  --lime-light:#c9dd52;
  --navy:#1c3a72;
  --navy-dark:#132a55;
  --ink:#1f3566;
  --stage:#e4e6e8;
  --white:#ffffff;
  --rule:#c9cfd8;
}
*{box-sizing:border-box;margin:0;padding:0}
html,body{width:1200px;height:5130px;overflow:hidden;background:var(--stage);font-family:"Arimo",Arial,sans-serif;color:var(--ink)}
.page{position:absolute;left:25px;width:1150px;height:960px;background:var(--white);box-shadow:0 2px 8px rgba(0,0,0,.18);overflow:hidden}
.brand{position:absolute;left:100px;top:0;width:262px;height:195px;background:var(--white);border:3px solid var(--navy);border-top:0;border-radius:0 0 16px 16px;display:flex;align-items:center;justify-content:center;gap:12px}
.brand-mark{width:26px;height:26px;background:var(--navy)}
.brand-name{font-family:"Krona One",sans-serif;font-size:26px;color:var(--navy);letter-spacing:1px}
.sidebar{position:absolute;left:150px;top:205px;width:190px;background:var(--lime);border-radius:0 0 12px 12px;padding:14px 12px 16px;color:var(--white)}
.side-link{display:flex;align-items:center;gap:8px;font-size:11px;font-weight:700;padding:6px 0;border-bottom:1px solid var(--lime-light)}
.side-link i{width:12px;height:12px;background:var(--navy);display:block}
.side-link.current{color:var(--navy)}
.contact{margin-top:18px;line-height:1.25}
.contact dt{font-size:9px;color:#eef5c4}
.contact dd{font-size:12px;font-weight:700;color:var(--navy);margin-bottom:8px}
.search{margin-top:16px;border-top:1px solid var(--lime-light);padding-top:10px}
.search-row{display:flex;align-items:center;justify-content:space-between;font-size:11px;font-weight:700;color:var(--navy)}
.search-row small{font-size:9px;display:flex;gap:6px;align-items:center}
.search-row small span::before{content:"";display:inline-block;width:9px;height:9px;border:1px solid var(--navy);border-radius:50%;background:#fff;margin-right:2px;vertical-align:-1px}
.search input{margin-top:8px;width:100%;height:22px;border:0;border-radius:3px;background:#fff}
.hero-photo{position:absolute;left:365px;top:0;width:165px;height:138px;background:linear-gradient(160deg,#f4f7fb 0%,#bcd3e8 55%,#3f6c9f 100%)}
.tagline{position:absolute;left:555px;top:72px;font-family:"Quicksand",sans-serif}
.tagline .soft{display:block;font-size:19px;color:var(--lime);font-weight:500}
.tagline .strong{display:block;margin:-6px 0 0 70px;font-size:26px;font-weight:700;color:var(--navy);letter-spacing:.5px}
.account{position:absolute;right:75px;top:16px;font-size:9px;font-weight:700;color:var(--navy)}
.account span{color:var(--rule);margin:0 4px}
.mainnav{position:absolute;left:365px;top:143px;width:710px;height:30px;background:var(--navy);border-radius:0 8px 8px 0;display:flex}
.mainnav a{display:flex;align-items:center;padding:0 12px;font-size:10px;font-weight:700;color:var(--white);text-decoration:none;border-right:2px solid var(--white)}
.mainnav a:last-child{border-right:0}
.mainnav a.active{background:var(--lime);color:var(--navy)}
.subnav{position:absolute;top:178px;display:flex;gap:18px;font-size:8px;font-weight:700;font-style:italic;color:var(--navy)}
.content{position:absolute;left:370px;top:215px}
.kicker{font-family:"Quicksand",sans-serif;font-size:24px;font-weight:700;color:var(--navy);line-height:1}
.headline{font-family:"Krona One",sans-serif;font-size:31px;color:var(--lime);line-height:1.1;margin-bottom:16px}
.copy{width:330px}
.copy p{font-size:9.5px;font-weight:700;line-height:16px;color:var(--ink);margin-bottom:14px}
.feature-art{position:absolute;left:720px;top:395px;width:360px;height:470px;border-radius:6px;background:radial-gradient(circle at 50% 50%,#dbe8a0 0%,#eef4cf 55%,#ffffff 80%)}
.footer{position:absolute;left:370px;top:818px;width:705px;border-top:3px solid var(--lime);padding-top:10px;font-size:9px;font-weight:700;color:var(--navy)}
/* locations */
.city-select{width:140px;height:22px;background:var(--lime);color:var(--navy);font-size:12px;font-weight:700;display:flex;align-items:center;justify-content:space-between;padding:0 6px;border:1px solid var(--navy-dark)}
.city-select svg{width:14px;height:10px}
.venues{margin-top:12px;font-size:9.5px;font-weight:700;line-height:15px;color:var(--navy);list-style:none}
.venues .area{color:var(--lime);margin-top:14px}
.venues .area:first-child{margin-top:0}
.map-area{position:absolute;left:545px;top:312px;width:515px;height:460px;border:1px solid var(--rule);background:linear-gradient(135deg,#d8e4f0 0%,#e9e4cf 45%,#c7d8b4 100%)}
/* forms */
.form-block{width:345px;border-bottom:1px solid var(--rule);padding-bottom:14px;margin-bottom:18px}
.form-block h3{font-size:12px;font-weight:700;color:var(--navy);margin-bottom:8px}
.field{display:flex;align-items:center;gap:8px;font-size:11px;color:var(--navy);margin-bottom:6px}
.field label{width:118px}
.field input{width:150px;height:14px;border:1px solid var(--lime)}
.btn{display:inline-block;margin-top:8px;padding:4px 12px;background:var(--lime);border:2px solid var(--lime-light);border-radius:12px;color:var(--white);font-size:10px;font-weight:700}
.radio{display:flex;align-items:center;gap:8px;font-size:11px;color:var(--navy);margin-bottom:6px}
.radio i{width:14px;height:14px;border-radius:50%;border:2px solid var(--lime);display:block}
.radio.on i{background:radial-gradient(circle,var(--navy) 40%,#fff 45%)}
.dropdowns{display:flex;gap:36px}
.dropdowns h4{font-size:11px;color:var(--navy);margin-bottom:6px}
.dropdowns h4 small{font-weight:400;font-size:9px}
.city-list{width:170px;list-style:none;font-size:12px;font-weight:700;color:var(--navy);background:var(--lime);border:1px solid var(--navy-dark)}
.city-list li{padding:3px 6px}
.city-list li.head{display:flex;justify-content:space-between;border-bottom:1px solid var(--navy-dark)}
.city-list li.hl{background:var(--navy);color:var(--white)}
</style>
</head>
<body>

<!-- Page 1: content page -->
<section class="page" style="top:33px">
  <div class="brand"><span class="brand-mark"></span><span class="brand-name">TALVREK</span></div>
  <div class="hero-photo" role="img" aria-label="Photo of a person working on a laptop by the water"></div>
  <div class="tagline"><span class="soft">get connected</span><span class="strong">anywhere you are</span></div>
  <div class="account">logout<span>|</span>account settings<span>|</span>welcome back, John</div>
  <nav class="mainnav"><a class="">HOME</a><a>WIRELESS HOTSPOTS</a><a>INTERNET KIOSKS</a><a>HOTSPOT LOCATIONS</a><a>RESELLERS</a><a>FAQ</a><a>CONTACT US</a></nav>
  <aside class="sidebar">
    <div class="side-link"><i></i>Jobs at Talvrek</div>
    <dl class="contact"><dt>email</dt><dd>freedom@talvrek.com</dd><dt>phone</dt><dd>1800 555 014</dd><dt>fax</dt><dd>(07) 5550 0123</dd></dl>
    <div class="search"><div class="search-row">Search<small><span>Web</span><span>Talvrek</span></small></div><input type="text" aria-label="Search"></div>
  </aside>
  <main class="content">
    <div class="kicker">welcome to</div>
    <h1 class="headline">WIRELESS FREEDOM</h1>
    <div class="copy">
      <p>Talvrek Wireless Solutions was founded to address the emerging and rapidly growing public demand for wireless internet access. A wireless hotspot service provision pioneer, we enable hotels, clubs, airports, motels, schools and universities, accommodation providers and cafes to offer a value added service that generates an additional revenue stream. Further information on our wireless hotspot system can be found here.</p>
      <p>Although a staggering 80% of the Australian population are now online, many are still tethered to their desks when accessing the internet. Talvrek's vision is to create a world of ubiquitous wireless internet access, without sacrificing the rich experience you get from your office, school, or home. In today's fast-moving world, people are used to being able to access the services they want, whenever and wherever they want them. Mobile professionals, everyday laptop-toting businessmen and students – they all need access to the internet at the push of a button, on the go.</p>
      <p>Wi-Fi is set to dramatically change the landscape of work and communication, more so than any technology since the advent of the internet. The progressive growth of Wi-Fi and its adoption across both large and small businesses, as well as through different vertical industries, means that it will soon become mainstream. All around the globe, publicly accessible wireless internet hotspots are springing up in airports, hotels, coffee shops, and restaurants. Those businesses slow on the uptake risk being left behind.</p>
    </div>
  </main>
  <div class="feature-art" style="top:395px" role="img" aria-label="Illustration of Australia made of green squares with photos of people using laptops: freedom at last, meetings on the go, connect with ease, communicate anywhere, when you need it the most"></div>
  <footer class="footer">©2009 Talvrek LTD</footer>
</section>

<!-- Page 2: wireless hotspots subnav -->
<section class="page" style="top:1059px">
  <div class="brand"><span class="brand-mark"></span><span class="brand-name">TALVREK</span></div>
  <div class="hero-photo" role="img" aria-label="Photo of a person working on a laptop by the water"></div>
  <div class="tagline"><span class="soft">get connected</span><span class="strong">anywhere you are</span></div>
  <div class="account">logout<span>|</span>account settings<span>|</span>welcome back, John</div>
  <nav class="mainnav"><a>HOME</a><a class="active">WIRELESS HOTSPOTS</a><a>INTERNET KIOSKS</a><a>HOTSPOT LOCATIONS</a><a>RESELLERS</a><a>FAQ</a><a>CONTACT US</a></nav>
  <div class="subnav" style="left:438px"><span>BENEFITS</span><span>DEMONSTRATION</span><span>FREE SITE SURVEY</span><span>HARDWARE &amp; SOFTWARE</span><span>HOW DOES IT WORK?</span></div>
  <aside class="sidebar">
    <div class="side-link"><i></i>Jobs at Talvrek</div>
    <dl class="contact"><dt>email</dt><dd>freedom@talvrek.com</dd><dt>phone</dt><dd>1800 555 014</dd><dt>fax</dt><dd>(07) 5550 0123</dd></dl>
    <div class="search"><div class="search-row">Search<small><span>Web</span><span>Talvrek</span></small></div><input type="text" aria-label="Search"></div>
  </aside>
  <main class="content">
    <div class="kicker">welcome to</div>
    <h1 class="headline">WIRELESS FREEDOM</h1>
    <div class="copy">
      <p>Talvrek Wireless Solutions was founded to address the emerging and rapidly growing public demand for wireless internet access. A wireless hotspot service provision pioneer, we enable hotels, clubs, airports, motels, schools and universities, accommodation providers and cafes to offer a value added service that generates an additional revenue stream. Further information on our wireless hotspot system can be found here.</p>
      <p>Although a staggering 80% of the Australian population are now online, many are still tethered to their desks when accessing the internet. Talvrek's vision is to create a world of ubiquitous wireless internet access, without sacrificing the rich experience you get from your office, school, or home. In today's fast-moving world, people are used to being able to access the services they want, whenever and wherever they want them. Mobile professionals, everyday laptop-toting businessmen and students – they all need access to the internet at the push of a button, on the go.</p>
      <p>Wi-Fi is set to dramatically change the landscape of work and communication, more so than any technology since the advent of the internet. The progressive growth of Wi-Fi and its adoption across both large and small businesses, as well as through different vertical industries, means that it will soon become mainstream. All around the globe, publicly accessible wireless internet hotspots are springing up in airports, hotels, coffee shops, and restaurants. Those businesses slow on the uptake risk being left behind.</p>
    </div>
  </main>
  <div class="feature-art" role="img" aria-label="Illustration of Australia made of green squares with photos of people using laptops"></div>
  <footer class="footer">©2009 Talvrek LTD</footer>
</section>

<!-- Page 3: hotspot locations subnav -->
<section class="page" style="top:2085px">
  <div class="brand"><span class="brand-mark"></span><span class="brand-name">TALVREK</span></div>
  <div class="hero-photo" role="img" aria-label="Photo of a person working on a laptop by the water"></div>
  <div class="tagline"><span class="soft">get connected</span><span class="strong">anywhere you are</span></div>
  <div class="account">logout<span>|</span>account settings<span>|</span>welcome back, John</div>
  <nav class="mainnav"><a>HOME</a><a>WIRELESS HOTSPOTS</a><a>INTERNET KIOSKS</a><a class="active">HOTSPOT LOCATIONS</a><a>RESELLERS</a><a>FAQ</a><a>CONTACT US</a></nav>
  <div class="subnav" style="left:545px"><span>HOTEL LOCATIONS</span><span>APARTMENT LOCATIONS</span><span>STUDENT LOCATIONS</span><span>OTHER LOCATIONS</span></div>
  <aside class="sidebar">
    <div class="side-link"><i></i>Jobs at Talvrek</div>
    <dl class="contact"><dt>email</dt><dd>freedom@talvrek.com</dd><dt>phone</dt><dd>1800 555 014</dd><dt>fax</dt><dd>(07) 5550 0123</dd></dl>
    <div class="search"><div class="search-row">Search<small><span>Web</span><span>Talvrek</span></small></div><input type="text" aria-label="Search"></div>
  </aside>
  <main class="content">
    <div class="kicker">welcome to</div>
    <h1 class="headline">WIRELESS FREEDOM</h1>
    <div class="copy">
      <p>Talvrek Wireless Solutions was founded to address the emerging and rapidly growing public demand for wireless internet access. A wireless hotspot service provision pioneer, we enable hotels, clubs, airports, motels, schools and universities, accommodation providers and cafes to offer a value added service that generates an additional revenue stream. Further information on our wireless hotspot system can be found here.</p>
      <p>Although a staggering 80% of the Australian population are now online, many are still tethered to their desks when accessing the internet. Talvrek's vision is to create a world of ubiquitous wireless internet access, without sacrificing the rich experience you get from your office, school, or home. In today's fast-moving world, people are used to being able to access the services they want, whenever and wherever they want them. Mobile professionals, everyday laptop-toting businessmen and students – they all need access to the internet at the push of a button, on the go.</p>
      <p>Wi-Fi is set to dramatically change the landscape of work and communication, more so than any technology since the advent of the internet. The progressive growth of Wi-Fi and its adoption across both large and small businesses, as well as through different vertical industries, means that it will soon become mainstream. All around the globe, publicly accessible wireless internet hotspots are springing up in airports, hotels, coffee shops, and restaurants. Those businesses slow on the uptake risk being left behind.</p>
    </div>
  </main>
  <div class="feature-art" role="img" aria-label="Illustration of Australia made of green squares with photos of people using laptops"></div>
  <footer class="footer">©2009 Talvrek LTD</footer>
</section>

<!-- Page 4: hotspot hotel locations -->
<section class="page" style="top:3111px">
  <div class="brand"><span class="brand-mark"></span><span class="brand-name">TALVREK</span></div>
  <div class="hero-photo" role="img" aria-label="Photo of a person working on a laptop by the water"></div>
  <div class="tagline"><span class="soft">get connected</span><span class="strong">anywhere you are</span></div>
  <div class="account">logout<span>|</span>account settings<span>|</span>welcome back, John</div>
  <nav class="mainnav"><a>HOME</a><a>WIRELESS HOTSPOTS</a><a>INTERNET KIOSKS</a><a class="active">HOTSPOT LOCATIONS</a><a>RESELLERS</a><a>FAQ</a><a>CONTACT US</a></nav>
  <aside class="sidebar">
    <div class="side-link current"><i></i>Hotel Locations</div>
    <div class="side-link"><i></i>Apartment Locations</div>
    <div class="side-link"><i></i>Student Locations</div>
    <div class="side-link"><i></i>Other Locations</div>
    <dl class="contact"><dt>email</dt><dd>freedom@talvrek.com</dd><dt>phone</dt><dd>1800 555 014</dd><dt>fax</dt><dd>(07) 5550 0123</dd></dl>
    <div class="search"><div class="search-row">Search<small><span>Web</span><span>Talvrek</span></small></div><input type="text" aria-label="Search"></div>
  </aside>
  <main class="content">
    <div class="kicker">hotspot hotel</div>
    <h1 class="headline">LOCATIONS</h1>
    <div class="city-select">Melbourne<svg viewBox="0 0 14 10"><path d="M1 1h12L7 9z" fill="#1c3a72"/></svg></div>
    <ul class="venues">
      <li class="area">Alice Springs</li>
      <li>Redgum Outback Inn</li><li>Ambassador Alice Lodge</li><li>Bendigo</li><li>Goldfields Central Stay</li><li>Quartz Inn Bendigo</li><li>Bowen</li><li>Coral Cove</li>
      <li class="area">Brisbane</li>
      <li>88 on Wattle</li><li>Runway Rest 12</li><li>Skyline Clayfield Motel</li><li>Banksia Apartments</li><li>Bellbird St Lodging</li><li>Kurrajong Motor Inn</li><li>Hillcrest Conference</li>
      <li class="area">Brisbane North</li>
      <li>River City Central</li><li>Ironbark Court Motel</li><li>Central Wattle</li><li>Northgate Motor Inn</li>
    </ul>
  </main>
  <div class="map-area" role="img" aria-label="Interactive map of Australia with hotspot pins clustered along the east coast"></div>
  <footer class="footer">©2009 Talvrek LTD</footer>
</section>

<!-- Page 5: forms example -->
<section class="page" style="top:4137px">
  <div class="brand"><span class="brand-mark"></span><span class="brand-name">TALVREK</span></div>
  <div class="hero-photo" role="img" aria-label="Photo of a person working on a laptop by the water"></div>
  <div class="tagline"><span class="soft">get connected</span><span class="strong">anywhere you are</span></div>
  <div class="account">logout<span>|</span>account settings<span>|</span>welcome back, John</div>
  <nav class="mainnav"><a>HOME</a><a>WIRELESS HOTSPOTS</a><a>INTERNET KIOSKS</a><a class="active">HOTSPOT LOCATIONS</a><a>RESELLERS</a><a>FAQ</a><a>CONTACT US</a></nav>
  <aside class="sidebar">
    <div class="side-link"><i></i>Jobs at Talvrek</div>
    <dl class="contact"><dt>email</dt><dd>freedom@talvrek.com</dd><dt>phone</dt><dd>1800 555 014</dd><dt>fax</dt><dd>(07) 5550 0123</dd></dl>
    <div class="search"><div class="search-row">Search<small><span>Web</span><span>Talvrek</span></small></div><input type="text" aria-label="Search"></div>
  </aside>
  <main class="content">
    <div class="kicker">forms page</div>
    <h1 class="headline">example</h1>
    <div class="form-block">
      <h3>Manage Your Account</h3>
      <div class="field"><label>Username / Email:</label><input type="text"></div>
      <div class="field"><label>Password:</label><input type="password"></div>
      <span class="btn">Submit</span>
    </div>
    <div class="form-block">
      <h3>Which Department would you like to contact?</h3>
      <div class="radio"><i></i>Support</div>
      <div class="radio on"><i></i>New Hotspot Location</div>
      <span class="btn">Submit</span>
    </div>
    <div class="dropdowns">
      <div>
        <h4>Which City? <small>(dropdown closed)</small></h4>
        <div class="city-select" style="width:170px">Melbourne<svg viewBox="0 0 14 10"><path d="M1 1h12L7 9z" fill="#1c3a72"/></svg></div>
      </div>
      <div>
        <h4>Which City? <small>(dropdown open)</small></h4>
        <ul class="city-list">
          <li class="head">Melbourne<svg width="14" height="10" viewBox="0 0 14 10"><path d="M1 1h12L7 9z" fill="#1c3a72"/></svg></li>
          <li>Brisbane</li><li class="hl">Gold Coast</li><li>Perth</li><li>Sydney</li><li>West Perth</li>
        </ul>
      </div>
    </div>
  </main>
  <footer class="footer">©2009 Talvrek LTD</footer>
</section>

</body>
</html>
```